New Brochure Design Project - downloadable PDF

Capability Statement, Brochure and Website - we are looking for a uniform of the three marketing assets that deliver a professional look and feel for executive-level decision-makers. Our company provides guest and patient-facing technologies. For the most part, the technologies are: smart TVs, Wi-Fi, RTLS, Integrated services. I have submitted the editable files we have, but in terms of industry images, we are happy to have others recommended. I have also submitted previous efforts and one Capability Statement from a company (QDN) that is well received.
Updates
Need extra days to review
Target Market(s)
Corporate and Government Procurement (Healthtcare and Hotels/Resorts)
Industry/Entity Type
Healthcare and Hotel/Resorts
Look and feel

```html
<!DOCTYPE html>
<html lang="en">
<head>
<meta charset="utf-8">
<title>HVN Corporate Profile – Executive Summary &amp; Core Competencies</title>
<link href="https://fonts.googleapis.com/css2?family=Roboto+Condensed:wght@300;400;700&display=swap" rel="stylesheet">
<style>
  :root {
    --brand-red: #e3161b;
    --ink: #2b2b2b;
    --paper: #ffffff;
    --backdrop: #e4e5e6;
    --photo-warm-a: #c9b8a6;
    --photo-warm-b: #6d5a4b;
    --photo-cool-a: #e9ecef;
    --photo-cool-b: #8f8a86;
    --device-a: #3a3a3a;
    --device-b: #111111;
  }
  * { box-sizing: border-box; margin: 0; padding: 0; }
  html, body { width: 1200px; height: 900px; overflow: hidden; }
  body {
    background: var(--backdrop);
    font-family: "Roboto Condensed", "Arial Narrow", sans-serif;
    color: var(--ink);
  }
  .spread {
    position: absolute; left: 40px; top: 20px;
    width: 1120px; height: 860px;
    display: flex;
  }
  .page {
    position: relative; width: 560px; height: 860px;
    background: var(--paper); overflow: hidden;
  }
  .photo { position: absolute; }
  .photo--meeting {
    left: 0; top: 0; width: 560px; height: 430px;
    background: linear-gradient(135deg, var(--photo-warm-a) 0%, #a48c78 45%, var(--photo-warm-b) 100%);
  }
  .accent-band {
    position: absolute; left: 0; top: 477px; width: 133px; height: 383px;
    background: var(--brand-red);
  }
  .section-title {
    font-weight: 400; color: var(--brand-red);
    font-size: 22px; letter-spacing: -0.2px;
  }
  .exec-summary {
    position: absolute; left: 169px; top: 474px; width: 350px;
  }
  .exec-summary .section-title { margin-bottom: 16px; }
  .body-copy p {
    font-size: 11.5px; line-height: 1.32; font-weight: 400;
    margin-bottom: 13px; letter-spacing: -0.2px;
  }
  .photo--device {
    left: 345px; top: 702px; width: 155px; height: 112px;
    border-radius: 16px;
    background: linear-gradient(160deg, var(--device-a), var(--device-b));
    box-shadow: 0 10px 14px rgba(0,0,0,.25);
  }
  .core {
    position: absolute; left: 38px; top: 42px; width: 230px;
  }
  .core .section-title { margin-bottom: 12px; }
  .core .lead {
    color: var(--brand-red); font-size: 13px; line-height: 1.3;
    margin-bottom: 18px;
  }
  .core .body-copy p {
    font-size: 10.5px; line-height: 1.36; text-align: justify; margin-bottom: 12px;
  }
  .vision {
    position: absolute; left: 309px; top: 0; width: 228px; height: 502px;
    background: var(--brand-red); color: #fff;
    padding: 44px 20px 0 20px;
  }
  .vision .section-title { color: #fff; margin-bottom: 14px; }
  .vision p, .vision li {
    font-size: 10.5px; line-height: 1.36; text-align: justify;
  }
  .vision ul { list-style: none; }
  .vision li { position: relative; padding-left: 11px; }
  .vision li::before {
    content: ""; position: absolute; left: 1px; top: 5px;
    width: 4px; height: 4px; border-radius: 50%; background: #fff;
  }
  .photo--lounge {
    left: 0; top: 550px; width: 560px; height: 310px;
    background: linear-gradient(120deg, #5a4a42 0%, var(--photo-cool-b) 35%, var(--photo-cool-a) 65%, #b9b2ab 100%);
  }
</style>
</head>
<body>
  <main class="spread">
    <section class="page page--left">
      <div class="photo photo--meeting" role="img" aria-label="Photo of three colleagues meeting around a café table with a laptop"></div>
      <div class="accent-band"></div>
      <article class="exec-summary">
        <h2 class="section-title">Executive Summary</h2>
        <div class="body-copy">
          <p>This corporate profile is intended to give a comprehensive overview of Harbourview Panel business operations.</p>
          <p>Harbourviewpanel is made up of several key business arms. There are Hospital &amp; Aged Care Centres, Hotels &amp; Mining Camps for guest services including WiFi, Movies on demand and content management and finance solutions for equipment acquisition and deployment for early adoption of the latest technologies.</p>
          <p>Our strength is through our continued evolution and improvement of services via close relationships with our customers.</p>
        </div>
      </article>
      <div class="photo photo--device" role="img" aria-label="Product photo of the HVN mini black set-top box"></div>
    </section>

    <section class="page page--right">
      <article class="core">
        <h2 class="section-title">Core Competencies</h2>
        <p class="lead">Innovation Solutions for In-Room Guest Services for the Accommodation, Mining and Healthcare markets.</p>
        <div class="body-copy">
          <p>HVN is a non-listed public company that provides technical services, entertainment and communication to hotels, resorts, mining camps and healthcare facilities.</p>
          <p>At HVN, our goal is to provide your patients with an easy to use system that will make their stay in hospital as enjoyable as possible, whilst benefiting the hospital and its staff in the provision of these services.</p>
          <p>HVNcare patient engagement solutions (PES) are a caring and consultative, long-term hospital partner. Our solutions are empowering to healthcare workers, patients, their families, and caregivers helping them meet their day-to-day challenges and improve their overall quality of life.</p>
          <p>HVN takes its reputation in the market very seriously and takes every care possible to work with the facilities to enhance that reputation within the Hospital community.</p>
          <p>With extensive industry experience, HVN is able to build the best outcomes together for this offering. HVNcare is a new generation software and hardware designed to meet the objectives of the Healthcare markets.</p>
        </div>
      </article>

      <aside class="vision">
        <h2 class="section-title">OUR VISION</h2>
        <p>To be the first-choice solution provider for accommodation guest/patient services, through dynamic and flexible integration platforms, extending to hospitals, aged care facilities, student, accommodation, and mining camps.</p>
        <ul>
          <li>Unique technology: HVN has developed a unique technology that delivers superior user entertainment services and Public Wi-Fi.</li>
          <li>Cost and revenue benefits: HVNcare is designed to improve the patient's experience, whilst promoting significant cost savings coupled with additional revenue streams for the Hospital.</li>
          <li>Customers: Current customers include hotels, hospitals, aged care facilities and remote accommodation facilities such as mining camps.</li>
          <li>Key geographic markets: Asia Pacific, North America.</li>
        </ul>
      </aside>

      <div class="photo photo--lounge" role="img" aria-label="Photo of a family on a sofa watching an on-demand movie menu on a television"></div>
    </section>
  </main>
</body>
</html>
```